Loopwave template for supermarket

I need a new fresh Loopwave template in which I can paste an image that changes depending on the content of the Loopwave post. I need to be able to change the design in Adobe Photoshop. It concerns the LW page of a local supermarket.
I once made a template myself, but I'm not satisfied with it.
Check the supermarket's website to see the supermarket's color scheme and style. The supermarket is a forerunner in the field of fresh products from local suppliers and has a wide range of organic products.
The slogan of the supermarket is 'At VENK we bring fresh meals, our street and one another'. The supermarket has a strong bond with the neighborhood and the inhabitants.
I have added my self-made template as an example. At the bottom right is the name of the owners of the supermarket.

```html
<!DOCTYPE html>
<html lang="nl">
<head>
<meta charset="utf-8">
<title>VENK – weekly meal post</title>
<link href="https://fonts.googleapis.com/css2?family=Oswald:wght@500&family=Kaushan+Script&family=Montserrat:wght@800&family=Nunito:wght@600&display=swap" rel="stylesheet">
<style>
  :root {
    --paper: #efeeeb;
    --lime: #78b51e;
    --lime-soft: #86c12a;
    --violet: #5a4fa6;
    --white: #ffffff;
    --placeholder-light: #f7f8f3;
    --placeholder-tint: #e3e9d8;
  }
  * { margin: 0; padding: 0; box-sizing: border-box; }
  html, body { width: 1200px; height: 1200px; overflow: hidden; background: var(--paper); }
  .post {
    position: relative;
    width: 1200px;
    height: 1200px;
    overflow: hidden;
    background: var(--paper);
  }
  .backdrop { position: absolute; inset: 0; width: 1200px; height: 1200px; }

  .headline-kicker {
    position: absolute;
    left: 450px;
    top: 98px;
    font-family: "Oswald", sans-serif;
    font-weight: 500;
    font-size: 66px;
    line-height: 1;
    color: var(--violet);
    white-space: nowrap;
  }
  .headline-script {
    position: absolute;
    left: 285px;
    top: 104px;
    font-family: "Kaushan Script", cursive;
    font-size: 210px;
    line-height: 1;
    color: var(--lime);
    white-space: nowrap;
  }
  .headline-accents { position: absolute; left: 0; top: 0; width: 1200px; height: 400px; }

  .meal-image-slot {
    position: absolute;
    left: 420px;
    top: 370px;
    width: 800px;
    height: 800px;
  }

  .price-badge {
    position: absolute;
    left: 110px;
    top: 420px;
    width: 314px;
    height: 314px;
    border: 15px solid var(--white);
    border-radius: 50% 50% 34px 50%;
    background: var(--violet);
    color: var(--white);
    box-shadow: 0 4px 14px rgba(0,0,0,0.12);
  }
  .price-amount {
    position: absolute;
    left: 48px;
    top: 56px;
    font-family: "Montserrat", sans-serif;
    font-weight: 800;
    font-size: 127px;
    line-height: 1;
    letter-spacing: -3px;
    white-space: nowrap;
  }
  .price-amount .cents {
    font-size: 68px;
    letter-spacing: -1px;
    vertical-align: top;
    position: relative;
    top: 2px;
    margin-left: -6px;
  }
  .price-rule {
    position: absolute;
    left: 36px;
    right: 36px;
    top: 182px;
    height: 3px;
    background: var(--white);
  }
  .price-unit {
    position: absolute;
    left: 0;
    right: 0;
    top: 192px;
    text-align: center;
    font-family: "Nunito", sans-serif;
    font-weight: 600;
    font-size: 36px;
    line-height: 1.1;
    white-space: nowrap;
  }

  .brand-name {
    position: absolute;
    left: 72px;
    top: 1048px;
    font-family: "Montserrat", sans-serif;
    font-weight: 800;
    font-size: 80px;
    line-height: 1;
    letter-spacing: 2px;
    color: var(--white);
  }
</style>
</head>
<body>
<main class="post">
  <svg class="backdrop" viewBox="0 0 1200 1200" aria-hidden="true">
    <path class="corner-wave" d="M0 0 H128 C96 44 48 100 0 138 Z" fill="var(--lime-soft)"/>
    <path class="ground-wave" d="M0 775 C150 880 320 905 480 872 C720 815 960 560 1200 340 L1200 1200 L0 1200 Z" fill="var(--lime)"/>
  </svg>

  <div class="headline-kicker">YOUR TEXT</div>
  <div class="headline-script">Here</div>
  <svg class="headline-accents" viewBox="0 0 1200 400" aria-hidden="true">
    <g stroke="var(--lime)" stroke-width="6" stroke-linecap="round" fill="none">
      <line x1="215" y1="165" x2="258" y2="200"/>
      <line x1="200" y1="232" x2="258" y2="235"/>
      <line x1="212" y1="298" x2="258" y2="272"/>
      <line x1="752" y1="182" x2="708" y2="222"/>
      <line x1="766" y1="252" x2="710" y2="258"/>
      <line x1="756" y1="318" x2="708" y2="292"/>
    </g>
  </svg>

  <svg class="meal-image-slot" viewBox="0 0 800 800" role="img" aria-label="Image placeholder: meal photo on a white plate, replaced per post">
    <defs>
      <linearGradient id="slotTone" x1="0" y1="0" x2="1" y2="1">
        <stop offset="0%" stop-color="var(--placeholder-light)"/>
        <stop offset="100%" stop-color="var(--placeholder-tint)"/>
      </linearGradient>
    </defs>
    <circle cx="398" cy="398" r="383" fill="url(#slotTone)"/>
  </svg>

  <div class="price-badge">
    <div class="price-amount">2.<span class="cents">75</span></div>
    <div class="price-rule"></div>
    <div class="price-unit">Per persoon</div>
  </div>

  <div class="brand-name">VENK</div>
</main>
</body>
</html>
```